Brightly Cleanse Hand Gel Label for Retail

We are currently supplying a product B2B but we are looking to enter the retail market, doing this we need a more attractive vibrant label, that still contains the information we need, I will attach the B2B label we are using for reference to some of the information we need.

I need 1 label in 2 sizes provided to me on a Photoshop File(so I can insert the right barcode).
Label 1 - 80mm Height
130mm Length

Label 2 - 60mm Height
100mm Length

We have been using Pantone 293C Blue as our main colour, this is not a preference although we would like blues to be used within.

The label will be used for a 70% hand gel, produced in 50ml + 100ml bottles, our line is a wrap around labeller hence the label sizes, we need a small gap in the centre of the label so it portrays to look front and back on the bottle, we would like the label to be transparent in places.

The ingredients, Warnings, Instructions for Use, BS EN 1500, BS EN 1276,
Kills 99.99% of Germs, Made in Britain. space for barcode need to be on the label.

The brand name is Brightly Cleanse

Target Market(s)

Retail

Industry/Entity Type

Health Product

Font styles to use
Sans Serif

Colors
3176b5
85acd3
83c9e6
85cae6
d4e3ef
85abd2

Requirements
Must have
• 'Brightly Cleanse'
Barcode
Warnings
Ingredients
Instructions of use
Made in Britain
Company Logo

```html
<!DOCTYPE html>
<html lang="en">
<head>
<meta charset="utf-8">
<title>Brightly Cleanse – Hand Gel Label</title>
<link href="https://fonts.googleapis.com/css2?family=Bebas+Neue&family=Arimo:wght@400;700&display=swap" rel="stylesheet">
<style>
  :root {
    --label-blue: #15476b;
    --label-blue-light: #1f6a96;
    --white: #ffffff;
    --heading-green: #4cc542;
    --badge-green: #5ed35a;
    --alert-red: #e3262d;
    --band-red: #d7182a;
    --ink-dark: #12324a;
  }
  * { margin: 0; padding: 0; box-sizing: border-box; }
  html, body { width: 739px; height: 1200px; overflow: hidden; background: var(--white); }
  .label {
    position: relative; width: 739px; height: 1200px; overflow: hidden;
    background: radial-gradient(circle at 25% 25%, var(--label-blue-light) 0%, var(--label-blue) 45%);
    font-family: 'Arimo', Arial, sans-serif; color: var(--white);
  }
  .display { font-family: 'Bebas Neue', 'Arial Narrow', sans-serif; font-weight: 400; }
  .abs { position: absolute; }

  /* front panel */
  .brand-name { left: 113px; top: 80px; width: 145px; text-align: center; font-size: 30px; font-weight: 700; letter-spacing: 1px; }
  .hero-art {
    left: 18px; top: 132px; width: 332px; height: 360px;
    background: radial-gradient(ellipse at 50% 38%, #e2262b 0%, #b81d24 42%, rgba(120,200,90,0.55) 72%, rgba(21,71,107,0) 100%);
    border-radius: 40% 40% 48% 48%;
  }
  .front-title { left: 18px; top: 192px; width: 332px; text-align: center; font-size: 76px; line-height: 68px; text-shadow: 0 3px 0 #8a1218; }
  .strength { left: 40px; top: 582px; width: 290px; text-align: center; color: var(--alert-red); font-size: 52px; line-height: 53px; }
  .badge-cross { left: 169px; top: 820px; z-index: 2; }
  .kill-badge {
    left: 109px; top: 828px; width: 158px; height: 158px; border-radius: 50%;
    background: var(--badge-green); color: var(--ink-dark); text-align: center; padding-top: 34px;
  }
  .kill-badge .small { font-size: 22px; line-height: 24px; }
  .kill-badge .big { font-size: 46px; line-height: 44px; }
  .volume { left: 122px; top: 997px; width: 114px; height: 38px; background: var(--band-red); text-align: center; font-size: 21px; font-weight: 700; line-height: 38px; }
  .origin { left: 21px; top: 1124px; display: flex; align-items: center; gap: 6px; font-size: 15px; font-weight: 700; line-height: 16px; }
  .flag-mark { width: 46px; height: 30px; background: linear-gradient(135deg, #2a3f8f, #ffffff 50%, #cf1f2e); }
  .standards-small { left: 270px; top: 1124px; font-size: 13px; line-height: 15px; }

  /* back panel */
  .back { left: 402px; width: 330px; white-space: nowrap; }
  .back-brand { left: 402px; top: 38px; width: 296px; text-align: center; font-size: 26px; font-weight: 700; letter-spacing: 1px; }
  .back-title { left: 402px; top: 80px; width: 296px; text-align: center; font-size: 66px; line-height: 57px; }
  .standards { left: 402px; top: 201px; width: 296px; text-align: center; font-size: 14px; line-height: 16px; }
  .section-heading { font-size: 17px; font-weight: 700; color: var(--heading-green); margin-bottom: 2px; }
  .section-heading.warning { color: var(--alert-red); }
  .info-text { font-size: 18px; line-height: 26px; }
  .info-list { list-style: none; font-size: 18px; line-height: 26px; }
  .info-list li { padding-left: 12px; text-indent: -12px; }
  .info-list li::before { content: "- "; }
  .ingredients { top: 248px; }
  .general { top: 392px; }
  .instructions { top: 537px; }
  .hazard-icons { left: 532px; top: 722px; display: flex; gap: 22px; }
  .warnings { top: 770px; }

  .barcode-space { left: 402px; top: 1005px; width: 105px; height: 136px; background: var(--white); }
  .company { left: 517px; top: 1000px; font-size: 17px; line-height: 20.5px; font-style: normal; }
  .company strong { font-weight: 700; }

  .danger-band {
    left: 0; top: 1170px; width: 739px; height: 30px; background: var(--band-red);
    text-align: center; font-size: 13px; font-weight: 700; letter-spacing: 1px; line-height: 30px;
  }
</style>
</head>
<body>
<main class="label">

  <!-- front panel -->
  <div class="abs brand-name">KELVARE</div>
  <div class="abs hero-art" role="img" aria-label="Red shield with cartoon green germ characters tumbling around it"></div>
  <h1 class="abs front-title display">Brightly<br>Cleanse</h1>
  <div class="abs strength display">70%<br>Alcohol<br>Gel</div>
  <div class="abs kill-badge display">
    <div class="small">Kills</div>
    <div class="big">99.99%</div>
    <div class="small">of germs</div>
  </div>
  <svg class="abs badge-cross" width="22" height="22" viewBox="0 0 22 22" aria-hidden="true">
    <path d="M7 0h8v7h7v8h-7v7H7v-7H0V7h7z" fill="var(--alert-red)"/>
  </svg>
  <div class="abs volume">100ml</div>
  <div class="abs origin">
    <div class="flag-mark" role="img" aria-label="Union flag"></div>
    <span>MADE IN<br>BRITAIN</span>
  </div>
  <div class="abs standards-small">BS EN 1500<br>BS EN 1276</div>

  <!-- back panel -->
  <div class="abs back-brand">KELVARE</div>
  <h2 class="abs back-title display">Brightly<br>Cleanse</h2>
  <div class="abs standards">BS EN 1500<br>BS EN 1276</div>

  <section class="abs back ingredients">
    <h3 class="section-heading">Ingredients:</h3>
    <p class="info-text">Active ingredient : Ethanol<br>Composition : Ethanol, Gylcerol,<br>Thickening agent and<br>Hydrogen peroxide</p>
  </section>

  <section class="abs back general">
    <h3 class="section-heading">General Information:</h3>
    <ul class="info-list">
      <li>WHO recommended formulation</li>
      <li>For external use only</li>
      <li>Avoid contact with eyes</li>
      <li>Keep out of the reach of Children</li>
    </ul>
  </section>

  <section class="abs back instructions">
    <h3 class="section-heading">Instructions for use:</h3>
    <ul class="info-list">
      <li>Ensure hand are washed, clean<br>and dry</li>
      <li>Apply a palmful of alcohol-based<br>gel and cover all surfaces of<br>the hands</li>
      <li>Rub hands until dry</li>
    </ul>
  </section>

  <div class="abs hazard-icons">
    <svg width="62" height="62" viewBox="0 0 62 62" aria-label="Flammable hazard" role="img">
      <path d="M31 2 60 31 31 60 2 31z" fill="var(--white)" stroke="var(--alert-red)" stroke-width="4"/>
      <path d="M31 16c6 8 11 12 11 21a11 11 0 0 1-22 0c0-5 3-8 5-10 0 4 2 6 4 6-1-6 0-11 2-17z" fill="#111"/>
      <rect x="19" y="46" width="24" height="3" fill="#111"/>
    </svg>
    <svg width="68" height="62" viewBox="0 0 68 62" aria-label="Irritant warning" role="img">
      <path d="M34 4 65 58H3z" fill="var(--white)" stroke="var(--alert-red)" stroke-width="5" stroke-linejoin="round"/>
      <rect x="31" y="20" width="6" height="22" rx="2" fill="#111"/>
      <circle cx="34" cy="49" r="3.5" fill="#111"/>
    </svg>
  </div>

  <section class="abs back warnings">
    <h3 class="section-heading warning">Warning:</h3>
    <ul class="info-list">
      <li>Highly flammable, Keep away<br>from flame or heat</li>
      <li>Causes serious eye irritation.</li>
      <li>If in eyes rinse eyes continuously<br>for several minutes.</li>
      <li>If any irrtation persists seek<br>medical advice and attention.</li>
    </ul>
  </section>

  <div class="abs barcode-space" role="img" aria-label="Space reserved for product barcode"></div>

  <address class="abs company">
    <strong>Kelvare Ltd.</strong><br>
    Unit 4, Meadowgate Court<br>
    12 Harlow Street,<br>
    Brackford<br>
    BK7 3QP<br>
    www.kelvare.co.uk<br>
    0161 555 0192
  </address>

  <div class="abs danger-band">DANGER : Flammable Vapour and liquid.&nbsp;&nbsp; IRRITANT : Can cause irritation to eyes.</div>
</main>
</body>
</html>
```